Email footer for a cafe

The task is to design an email footer for a new start up cafe business. The logo has been designed, but we would like a professional email footer to sign off on all emails.

The email footer should :
1. look professional and competent
2. be clean and easy to read
3. the email must have the ability to optimise / adjust across the bottom of the email depending on the device being used to read the email
4. the design may stretch across the entire bottom of the email, but this is not mandatory
5. it must incorporate the logo and the details as listed below.
6. For any additional lines / dividers that a designer might choose to incorporate into the email footer, our preference is to match the colour of the logo.

The logo is attached. The logo details are:

The CMYK for the logo is C0 M50 Y100 K0 in font BankGothic Lt BT - Light
The CMKY for the text is C75 M68 Y67 K89 in font AvantGarde Bk BT - Book

The details to be included in the email footer are:

Ted Varro
Founder
0417 283 614
pelvar@brookfieldkitchenqx.com
Unit 6, 14 Malvory Crescent
Tembly KLW 5213

Have fun and thank you in advance for choosing to work on our job.

Reason: Thank you to everyone who has submitted their designs for an email footer. Looking at the designs most have been designed horizontally. Could I please also see some designs where all the elements are under each other in a stacked format. I have attached 2 images which I have grabbed from the internet to be used as an example.

```html
<!DOCTYPE html>
<html lang="en">
<head>
<meta charset="utf-8">
<title>Brookfield Kitchen – Email Footer</title>
<link href="https://fonts.googleapis.com/css2?family=Copse&family=Saira+Semi+Condensed:wght@400&display=swap" rel="stylesheet">
<style>
  :root {
    --stage: #000000;
    --card: #ffffff;
    --brand-orange: #f7941d;
    --text-dark: #231f20;
    --on-orange: #ffffff;
  }
  html, body {
    margin: 0;
    padding: 0;
    width: 1200px;
    height: 1200px;
    overflow: hidden;
    background: var(--stage);
  }
  .canvas {
    position: relative;
    width: 1200px;
    height: 1200px;
    background: var(--stage);
  }
  .footer-card {
    position: absolute;
    left: 320px;
    top: 380px;
    width: 560px;
    height: 440px;
    box-sizing: border-box;
    padding: 44px 48px;
    background: var(--card);
    display: flex;
    flex-direction: column;
    align-items: flex-start;
  }
  .brand {
    display: flex;
    align-items: center;
    gap: 14px;
    margin: 0;
  }
  .brand-mark {
    display: block;
    flex: none;
  }
  .brand-name {
    margin: 0;
    font-family: "Copse", serif;
    font-weight: 400;
    font-size: 34px;
    line-height: 40px;
    letter-spacing: 2px;
    color: var(--brand-orange);
    white-space: nowrap;
  }
  .divider {
    width: 100%;
    height: 0;
    border: 0;
    border-top: 2px solid var(--brand-orange);
    margin: 28px 0 28px;
  }
  .identity {
    display: flex;
    align-items: center;
    gap: 12px;
    height: 52px;
  }
  .person-name {
    margin: 0;
    height: 52px;
    padding: 0 12px;
    background: var(--brand-orange);
    color: var(--on-orange);
    font-family: "Saira Semi Condensed", sans-serif;
    font-weight: 400;
    font-size: 36px;
    line-height: 52px;
    white-space: nowrap;
  }
  .person-role {
    margin: 0;
    padding-top: 4px;
    color: var(--brand-orange);
    font-family: "Copse", serif;
    font-size: 36px;
    line-height: 48px;
  }
  .contact {
    list-style: none;
    margin: 22px 0 0;
    padding: 0;
    font-family: "Copse", serif;
    font-size: 21px;
    line-height: 30px;
    color: var(--text-dark);
  }
</style>
</head>
<body>
<div class="canvas">
  <footer class="footer-card">
    <div class="brand">
      <svg class="brand-mark" width="36" height="36" viewBox="0 0 36 36" aria-hidden="true">
        <circle cx="18" cy="18" r="18" fill="var(--brand-orange)"/>
      </svg>
      <p class="brand-name">BROOKFIELD KITCHEN</p>
    </div>
    <hr class="divider">
    <div class="identity">
      <h1 class="person-name">Ted Varro</h1>
      <p class="person-role">Founder</p>
    </div>
    <ul class="contact">
      <li>Dail: 0417 283 614</li>
      <li>pelvar@brookfieldkitchenqx.com</li>
      <li>Unit 6, 14 Malvory Crescent</li>
      <li>Tembly KLW 5213</li>
    </ul>
  </footer>
</div>
</body>
</html>
```